Marrowind Lake Billboard

Looking to design a multi purpose billboard promoting Marrowind Lake as a destination point. Billboard size is 12ft x 40ft
My goal is to advertise our restaurant The Driftmill (pic attached)
What makes Marrowind a destination? It offers lodging / water skiing / Off Road Adventure / Camping / Fishing / Hunting
Want a catch phrase, something like "Looking For a Getaway" or "Need a Break"
Needs to really pop and catch the interest of the looker
maybe have our website address www.marrowinddriftmill.example
Open for ideas

```html
<!DOCTYPE html>
<html lang="en">
<head>
<meta charset="utf-8">
<title>Marrowind Lake Billboard</title>
<link rel="stylesheet" href="https://fonts.googleapis.com/css2?family=Barlow:wght@400;600&family=Montserrat:ital,wght@0,600;0,700;0,800;1,800&display=swap">
<style>
  :root {
    --brand-green: #4f9d4e;
    --band-green: #519e4e;
    --panel-dark: #10170f;
    --orange: #d3772b;
    --red: #e0262b;
    --deep-green: #1f5c35;
    --white: #ffffff;
  }
  * { margin: 0; padding: 0; box-sizing: border-box; }
  html, body { width: 1200px; height: 849px; overflow: hidden; background: var(--white); }
  .board {
    position: relative;
    width: 1200px;
    height: 849px;
    background: linear-gradient(to bottom, var(--white) 0 397px, var(--band-green) 397px 100%);
  }
  .board-title {
    position: absolute;
    top: 118px;
    width: 100%;
    text-align: center;
    font-family: "Barlow", sans-serif;
    font-weight: 600;
    font-size: 52px;
    letter-spacing: 0.5px;
    color: var(--brand-green);
  }
  .board-subtitle {
    position: absolute;
    top: 202px;
    width: 100%;
    text-align: center;
    font-family: "Barlow", sans-serif;
    font-weight: 400;
    font-size: 23px;
    line-height: 28px;
    letter-spacing: 0.6px;
    color: var(--brand-green);
  }
  .billboard {
    position: absolute;
    left: 21px;
    top: 368px;
    width: 1157px;
    height: 289px;
    filter: drop-shadow(0 6px 10px rgba(0,0,0,0.45));
  }
  .billboard text { font-family: "Montserrat", sans-serif; }
  .headline { fill: var(--white); font-weight: 700; font-size: 32px; letter-spacing: -0.8px; }
  .lake-name { fill: var(--white); font-weight: 800; font-size: 34px; letter-spacing: -0.8px; }
  .badge-text { fill: var(--white); font-weight: 800; font-size: 11px; }
  .attractions-label { fill: var(--brand-green); font-weight: 700; font-size: 12.5px; letter-spacing: -0.4px; }
  .attraction { fill: var(--orange); font-weight: 700; font-size: 12.5px; letter-spacing: -0.4px; }
  .tagline { fill: var(--white); font-weight: 800; font-style: italic; letter-spacing: -0.6px; }
  .tagline-large { font-size: 23px; }
  .tagline-small { font-size: 19px; }
  .tagline-dark { fill: var(--deep-green); font-weight: 800; font-style: italic; font-size: 20px; letter-spacing: -0.6px; }
  .web-address { fill: var(--white); font-weight: 800; font-style: italic; font-size: 12.5px; letter-spacing: -0.5px; }
  .emblem-name { fill: var(--white); font-weight: 700; font-size: 13px; }
</style>
</head>
<body>
<main class="board">
  <h1 class="board-title">Marrowind Lake Billboard</h1>
  <p class="board-subtitle">a multi purpose billboard promoting<br>Marrowind Lake as a destination point</p>

  <svg class="billboard" viewBox="0 0 1157 289" xmlns="http://www.w3.org/2000/svg">
    <defs>
      <radialGradient id="store-tones" cx="0.55" cy="0.72" r="0.75">
        <stop offset="0" stop-color="#c9782e"/>
        <stop offset="0.3" stop-color="#8c4f22"/>
        <stop offset="0.6" stop-color="#4b3220"/>
        <stop offset="1" stop-color="#1a2016"/>
      </radialGradient>
      <radialGradient id="wrap-tones" cx="0.6" cy="0.55" r="0.8">
        <stop offset="0" stop-color="#d8543a"/>
        <stop offset="0.3" stop-color="#7fa847"/>
        <stop offset="0.65" stop-color="#d9b07a"/>
        <stop offset="1" stop-color="#8a4a24"/>
      </radialGradient>
      <radialGradient id="ribs-tones" cx="0.5" cy="0.5" r="0.7">
        <stop offset="0" stop-color="#d0652e"/>
        <stop offset="0.5" stop-color="#8e3c1c"/>
        <stop offset="1" stop-color="#3e3a36"/>
      </radialGradient>
      <linearGradient id="sunrise-tones" x1="0" y1="0" x2="0" y2="1">
        <stop offset="0" stop-color="#5a6fa8"/>
        <stop offset="0.4" stop-color="#b07a8e"/>
        <stop offset="0.6" stop-color="#e86a3a"/>
        <stop offset="0.68" stop-color="#3a2e2c"/>
        <stop offset="0.78" stop-color="#c9603a"/>
        <stop offset="1" stop-color="#55607c"/>
      </linearGradient>
    </defs>

    <!-- store scene -->
    <polygon role="img" aria-label="Lakeside restaurant and bait shop lit with warm lights at dusk" points="280,0 746,0 667,289 199,289" fill="url(#store-tones)"/>

    <!-- food column -->
    <polygon points="742,0 1006,0 927,289 663,289" fill="var(--white)"/>
    <polygon role="img" aria-label="Grilled wrap with lettuce and tomato beside waffle fries" points="750,0 998,0 959,144 711,144" fill="url(#wrap-tones)"/>
    <polygon role="img" aria-label="Racks of barbecue ribs on a grill" points="701,185 949,185 919,289 672,289" fill="url(#ribs-tones)"/>
    <text class="tagline-dark" x="817" y="173" text-anchor="middle">Taste the food</text>

    <!-- sunrise -->
    <polygon role="img" aria-label="Sunrise over the lake with a wooded shoreline" points="1006,0 1157,0 1157,289 927,289" fill="url(#sunrise-tones)"/>
    <g class="emblem">
      <text class="emblem-name" x="1063" y="112" text-anchor="middle">Harbor Light</text>
      <circle cx="1063" cy="148" r="16" fill="none" stroke="var(--white)" stroke-width="2"/>
    </g>
    <polygon points="950,220 1157,220 1157,260 939,260" fill="var(--brand-green)"/>
    <text class="tagline tagline-small" x="956" y="246">Catch our sunrise</text>

    <!-- left panel -->
    <polygon points="0,0 284,0 203,289 0,289" fill="var(--panel-dark)"/>
    <polygon points="284,0 292,0 211,289 203,289" fill="var(--white)"/>

    <text class="headline" x="37" y="55">Looking For a</text>
    <text class="headline" x="37" y="92">Getaway?</text>

    <path d="M0,106 H327 A29.5,29.5 0 0 1 327,165 H0 Z" fill="var(--orange)"/>
    <text class="lake-name" x="37" y="150">Marrowind Lake</text>

    <g class="come-try-badge" transform="rotate(-10 227 85)">
      <circle cx="227" cy="85" r="27" fill="var(--red)"/>
      <circle cx="227" cy="85" r="23" fill="none" stroke="var(--white)" stroke-width="0.8" stroke-dasharray="2 2"/>
      <text class="badge-text" x="227" y="84" text-anchor="middle">COME</text>
      <text class="badge-text" x="227" y="96" text-anchor="middle">&amp; TRY</text>
    </g>

    <text class="attractions-label" x="39" y="194">ATTRACTIONS:</text>
    <text class="attraction" x="39" y="217">lodging/water skiing</text>
    <text class="attraction" x="39" y="232">Fishing/Off Road/Adventure</text>
    <text class="attraction" x="39" y="247">Camping &amp; Hunting</text>

    <!-- partner badge -->
    <circle cx="306" cy="246" r="37" fill="var(--white)" stroke="#555" stroke-width="1.5"/>

    <!-- restaurant callout -->
    <polygon points="412,222 684,222 673,260 401,260" fill="var(--brand-green)"/>
    <text class="tagline tagline-large" x="538" y="250" text-anchor="middle">Visit the Driftmill</text>
    <text class="web-address" x="530" y="277" text-anchor="middle">www.marrowinddriftmill.example</text>
  </svg>
</main>
</body>
</html>
```